High Quality fast food restaurant - Tomanyo

Tomanyo is a fast food company with its target's focused on logistic, simplicity, high quality, freshness and modern.

We need a web design where the customers can get a complete idea of our high quality completeness, we want to take fast food to a new upper level.

We would like to see the colours of wood and metal. Pictures have been attached of our local.

We would like to have something in similar to: http://www.qpz.example/
Updates

Images for the food we are going to sell can be found here: http://shrt.example/uWQa7

It will be the images with rice, french fries or pita bread.

Target Market(s)

The fast food eating people between sloppy food and restaurant level.

Industry/Entity Type

Fast Food Restaurant

Requirements
Should not have
• No Flash or Java

```html
<!DOCTYPE html>
<html lang="en">
<head>
<meta charset="utf-8">
<title>Tomanyo – High Quality Fast Food</title>
<link rel="stylesheet" href="https://fonts.googleapis.com/css2?family=Cinzel:wght@400;700;900&family=Roboto:wght@700&family=Archivo+Black&family=Oswald:wght@600&family=Arimo:wght@400;700&display=swap">
<style>
:root{
  --wood-dark:#3a1408;
  --wood-mid:#7a2a10;
  --wood-red:#8e3315;
  --nav-top:#c0400f;
  --nav-bottom:#6e1d06;
  --panel-light:#f0cf9d;
  --panel-mid:#e2b57c;
  --frame:#5a1e08;
  --ink:#7a2a12;
  --ink-dark:#5a1d0a;
  --cream:#f6e0c0;
  --white:#ffffff;
}
*{margin:0;padding:0;box-sizing:border-box}
html,body{width:1200px;height:1196px;overflow:hidden}
body{
  position:relative;
  background:
    linear-gradient(180deg,rgba(0,0,0,.25),rgba(0,0,0,0) 30%,rgba(0,0,0,.2)),
    repeating-linear-gradient(178deg,#7d2c12 0 18px,#8f3718 18px 34px,#6f240d 34px 52px),
    var(--wood-mid);
  font-family:"Arimo",Arial,sans-serif;
}
.site-header{position:absolute;left:0;top:0;width:1200px;height:132px;
  background:linear-gradient(180deg,#2a0f07,#3b170b 70%,#2c1008);text-align:center}
.brand{position:absolute;left:0;right:0;top:18px;font-family:"Cinzel",serif;font-weight:900;
  font-size:58px;color:var(--white);letter-spacing:2px;line-height:1}
.tagline{position:absolute;left:0;right:0;top:88px;font-family:"Roboto",sans-serif;font-weight:700;
  font-size:18px;color:var(--white)}
.nav-band{position:absolute;left:0;top:160px;width:1200px;height:47px;background:#4a1606}
.main-nav a{position:absolute;top:148px;height:59px;display:flex;align-items:center;justify-content:center;
  font-family:"Cinzel",serif;font-size:14px;font-weight:700;color:var(--cream);text-decoration:none;letter-spacing:.5px;
  background:linear-gradient(180deg,var(--nav-top),var(--nav-bottom));border-top:1px solid #e0703a}
.main-nav a.active{background:linear-gradient(180deg,#d24a10,#b8380c);color:var(--white)}
.slider{position:absolute;left:169px;top:224px;width:861px;height:296px;background:var(--frame);border:1px solid #9c4a20}
.slide-photo{position:absolute;top:4px;height:287px}
.slide-photo.burger{left:4px;width:355px;background:radial-gradient(ellipse at 50% 50%,#a0501f,#d59b55 55%,#fbf6ef 75%)}
.slide-photo.dessert{left:359px;width:497px;background:radial-gradient(ellipse at 60% 30%,#f3ead6,#b55a3a 40%,#5a2218 75%)}
.slide-title{position:absolute;left:415px;top:98px;font-family:"Archivo Black",sans-serif;font-size:28px;line-height:34px;color:var(--white);letter-spacing:1px}
.slide-btn{position:absolute;left:423px;top:188px;width:176px;height:50px;display:flex;align-items:center;justify-content:center;
  font-family:"Oswald",sans-serif;font-size:21px;color:var(--white);background:linear-gradient(180deg,#c0410f,#8e2a08);border-radius:3px;text-decoration:none}
.arrow{position:absolute;top:118px;width:33px;height:48px;background:#1e0a05}
.arrow.prev{left:359px}.arrow.next{left:827px}
.dots{position:absolute;left:367px;top:270px;display:flex;gap:5px}
.dots span{width:15px;height:15px;border-radius:50%;background:#5a1a08}
.dots span.on{background:#c23a10}
.content{position:absolute;left:169px;top:527px;width:861px;height:458px;border:4px solid var(--frame);
  background:linear-gradient(90deg,var(--panel-mid),var(--panel-light) 40%,var(--panel-mid));box-shadow:0 0 0 1px #a24b22}
.section-title{position:absolute;font-family:"Cinzel",serif;font-size:15px;color:var(--ink-dark);display:flex;align-items:center;gap:10px;white-space:nowrap}
.section-title::before,.section-title::after{content:"";height:7px;flex:1;
  background:linear-gradient(var(--ink-dark),var(--ink-dark)) 0 3px/100% 1px no-repeat,
  linear-gradient(var(--ink-dark),var(--ink-dark)) right 0/28px 1px no-repeat,
  linear-gradient(var(--ink-dark),var(--ink-dark)) right 6px/28px 1px no-repeat}
.section-title::after{background:linear-gradient(var(--ink-dark),var(--ink-dark)) 0 3px/100% 1px no-repeat,
  linear-gradient(var(--ink-dark),var(--ink-dark)) left 0/28px 1px no-repeat,
  linear-gradient(var(--ink-dark),var(--ink-dark)) left 6px/28px 1px no-repeat}
.thumb{position:absolute;border:5px solid #c88a55;box-shadow:0 0 0 1px #9a5a2c}
.thumb.bar{background:linear-gradient(160deg,#3a1a10,#1a0c08 60%,#7a1a12)}
.thumb.soup{background:radial-gradient(ellipse at 50% 55%,#d0602a,#c87a40 35%,#eef0f2 60%,#4a3a30)}
.thumb.crowd{background:linear-gradient(180deg,#4a3020,#1e120c)}
.thumb.shop{background:linear-gradient(90deg,#3f6d64 0 40%,#4a2a2a 40%,#2a1a1a)}
.welcome-text{position:absolute;left:316px;top:275px;width:524px;font-size:10.5px;line-height:15.8px;color:#8a2c12;text-align:justify}
.welcome-text p+p{margin-top:15px}
.signup{position:absolute;left:169px;top:995px;width:861px;height:118px;border:4px solid var(--frame);
  background:linear-gradient(90deg,var(--panel-mid),var(--panel-light) 40%,var(--panel-mid));box-shadow:0 0 0 1px #a24b22}
.col-divider{position:absolute;top:0;bottom:0;width:1px;background:#9a5a30}
.block-title{position:absolute;font-family:"Cinzel",serif;font-size:14px;line-height:16px;color:var(--ink-dark);text-align:center;letter-spacing:.5px}
.field{position:absolute;height:31px;display:flex;border-radius:5px;overflow:hidden;background:linear-gradient(180deg,#c8420f,#8a2a08);border:1px solid #6a1e06}
.field span{flex:1;padding-left:12px;display:flex;align-items:center;font-size:11px;color:#f5d7bd}
.field b{display:flex;align-items:center;padding:0 11px;font-size:11.5px;color:var(--white);background:#7e2508;font-weight:700}
.contact-name{position:absolute;left:653px;top:12px;font-family:"Cinzel",serif;font-size:24px;color:#9a3a14}
.contact-lines{position:absolute;left:668px;top:52px;font-size:10.5px;line-height:16px;color:#8a2c12}
.social{position:absolute;left:819px;width:28px;height:28px;border-radius:4px;background:linear-gradient(180deg,#b5501e,#7e2a0a)}
.footer-links{position:absolute;left:0;right:0;top:1134px;text-align:center;font-family:"Cinzel",serif;font-size:12px;font-weight:700;color:#e8b07a}
.footer-links a{color:#e8b07a;text-decoration:none;margin:0 4px}
.copyright{position:absolute;left:0;right:0;top:1158px;text-align:center;font-family:"Cinzel",serif;font-size:11px;font-weight:700;color:#e0a070}
</style>
</head>
<body>
<header class="site-header">
  <div class="brand">TOMANYO</div>
  <div class="tagline">Heigh Quality Fast Food</div>
</header>
<div class="nav-band"></div>
<nav class="main-nav">
  <a class="active" href="#" style="left:171px;width:77px">Menu</a>
  <a href="#" style="left:264px;width:143px">Fresh Offers</a>
  <a href="#" style="left:421px;width:139px">Crown Card</a>
  <a href="#" style="left:576px;width:104px">Delivers</a>
  <a href="#" style="left:695px;width:133px">Location</a>
  <a href="#" style="left:842px;width:188px">Company Info</a>
</nav>

<section class="slider">
  <div class="slide-photo burger" role="img" aria-label="Cheeseburger with lettuce and tomato"></div>
  <div class="slide-photo dessert" role="img" aria-label="Berry crumble dessert topped with ice cream"></div>
  <div class="slide-title">GIVE THE GIFT<br>THAT'S ALWAYS IN</div>
  <a class="slide-btn" href="#">VIEW MORE RECIPES</a>
  <svg class="arrow prev" viewBox="0 0 33 48"><path d="M21 13 11 24l10 11" fill="none" stroke="#fff" stroke-width="4"/></svg>
  <svg class="arrow next" viewBox="0 0 33 48"><path d="M12 13l10 11-10 11" fill="none" stroke="#fff" stroke-width="4"/></svg>
  <div class="dots"><span></span><span class="on"></span><span></span><span></span></div>
</section>

<main class="content">
  <h2 class="section-title" style="left:18px;top:24px;width:246px">Drink Menu</h2>
  <h2 class="section-title" style="left:306px;top:24px;width:246px">Food Menu</h2>
  <h2 class="section-title" style="left:592px;top:24px;width:246px">About Us</h2>
  <div class="thumb bar" role="img" aria-label="Restaurant bar interior with red chairs" style="left:18px;top:55px;width:246px;height:145px"></div>
  <div class="thumb soup" role="img" aria-label="Bowl of minestrone soup" style="left:306px;top:55px;width:246px;height:145px"></div>
  <div class="thumb crowd" role="img" aria-label="Guests at the restaurant bar" style="left:592px;top:55px;width:246px;height:145px"></div>
  <h2 class="section-title" style="left:117px;top:238px;width:630px">Welcome to Tomanyo</h2>
  <div class="thumb shop" role="img" aria-label="Tomanyo restaurant storefront" style="left:14px;top:272px;width:292px;height:149px"></div>
  <div class="welcome-text">
    <p>Lorem ipsum dolor sit amet, consectetur adipisicing elit, sed do eiusmod tempor incididunt ut labore et dolore magna aliqua. Ut enim ad minim veniam, quis nostrud exercitation ullamco laboris nisi ut aliquip ex ea commodo consequat. Duis aute irure dolor in reprehenderit in voluptate velit esse cillum dolore eu fugiat nulla pariatur. Excepteur sint occaecat cupidatat non proident, sunt in culpa qui officia deserunt mollit anim id est laborum.</p>
    <p>At vero eos et accusamus et iusto odio dignissimos ducimus qui blanditiis praesentium voluptatum deleniti atque corrupti quos dolores et quas molestias excepturi sint occaecati cupiditate non provident, similique sunt in culpa qui officia deserunt mollitia animi, id est laborum et dolorum fuga. Et harum quidem rerum facilis est et expedita distinctio. Nam libero tempore, cum soluta nobis est eligendi optio cumque nihil</p>
  </div>
</main>

<section class="signup">
  <div class="col-divider" style="left:284px"></div>
  <div class="col-divider" style="left:582px"></div>
  <div class="block-title" style="left:20px;top:26px;width:250px">Sign up for News and<br>Special Offers</div>
  <div class="field" style="left:33px;top:65px;width:215px"><span>Enter your Email</span><b>SUBMIT</b></div>
  <div class="block-title" style="left:300px;top:26px;width:270px">Search for Our<br>Events</div>
  <div class="field" style="left:322px;top:65px;width:215px"><span>Search....</span><b>GO NOW</b></div>
  <div class="contact-name">TOMANYO</div>
  <svg style="position:absolute;left:616px;top:46px" width="42" height="48" viewBox="0 0 42 48">
    <rect x="9" y="5" width="24" height="38" rx="5" transform="rotate(15 21 24)" fill="#f6e6cc" stroke="#7a2a12" stroke-width="2.5"/>
    <g fill="#7a2a12"><circle cx="19" cy="22" r="1.6"/><circle cx="24" cy="23" r="1.6"/><circle cx="17" cy="27" r="1.6"/><circle cx="22" cy="28" r="1.6"/><circle cx="15" cy="32" r="1.6"/><circle cx="20" cy="33" r="1.6"/></g>
  </svg>
  <div class="contact-lines">Phone: (555) 0142 6630<br>Fax: 555 018<br>Email: info@tomanyo.example</div>
  <span class="social" style="top:10px"></span>
  <span class="social" style="top:46px"></span>
  <span class="social" style="top:82px"></span>
</section>

<nav class="footer-links">
  <a href="#">HOME</a>|<a href="#">FOOD</a>|<a href="#">DRINK</a>|<a href="#">FRESH OFFER</a>|<a href="#">GALLERY</a>|<a href="#">LOCATION</a>|<a href="#">CONTACT US</a>
</nav>
<div class="copyright">© 2013 TOMANYO CORPORATION. ALL RIGHTS RESERVED.</div>
</body>
</html>
```